Small Business Consulting Firm Needs Business Card Design

Need a sleek modern business card with 2 sides matching the colors of our logo. We will be placing these with a mailer we are sending out. These business cards will only ever be given to business owners. We operate helping businesses who are struggling with cash flow or finances. If the green and blue design needs to be moved to the right of "Harborline Crest Consulting" for aesthetic purposes that is ok. We will need an editable file if possible. We would like to include the reps name, email, website, and phone number. For now just use Peter Vance, pvance@harborlinecrest.com, www.harborlinecrest.com, and 833-555-0172.

```html
<!DOCTYPE html>
<html lang="en">
<head>
<meta charset="utf-8">
<title>Harborline Crest Consulting – Business Card</title>
<link href="https://fonts.googleapis.com/css2?family=Montserrat:wght@400;500;600&display=swap" rel="stylesheet">
<style>
  :root {
    --stage: #e9ebee;
    --card: #ffffff;
    --brand-blue: #1b6fc0;
    --brand-green: #6ab23a;
    --tint-blue: #bcdcef;
    --tint-blue-soft: #d3e8f4;
    --tint-green: #cfe3b6;
    --tint-green-soft: #e0edd0;
    --ink: #4a4a4a;
    --ink-soft: #6b6b6b;
    --rule: #9a9a9a;
  }
  * { box-sizing: border-box; margin: 0; padding: 0; }
  html, body { width: 1200px; height: 1000px; overflow: hidden; }
  body {
    background: var(--stage);
    font-family: "Montserrat", Arial, sans-serif;
    display: flex;
    flex-direction: column;
    align-items: center;
    justify-content: center;
    gap: 60px;
  }
  .card {
    position: relative;
    width: 700px;
    height: 400px;
    background: var(--card);
    border-radius: 26px;
    overflow: hidden;
    box-shadow: 0 10px 30px rgba(0,0,0,0.12);
  }

  /* Front */
  .side-band {
    position: absolute;
    top: 0;
    bottom: 0;
    width: 140px;
  }
  .side-band-left {
    left: 0;
    background: linear-gradient(180deg, var(--tint-blue-soft), var(--tint-blue));
  }
  .side-band-right {
    right: 0;
    background: linear-gradient(180deg, var(--tint-green-soft), var(--tint-green));
  }
  .brand-lockup {
    display: flex;
    align-items: center;
    gap: 16px;
  }
  .card-front .brand-lockup {
    position: absolute;
    left: 50%;
    top: 50%;
    transform: translate(-50%, -50%);
  }
  .brand-mark {
    width: 20px;
    height: 20px;
    background: var(--brand-blue);
    flex: none;
  }
  .brand-name {
    color: var(--ink);
    font-weight: 400;
    text-transform: uppercase;
    white-space: nowrap;
    line-height: 1.2;
  }
  .brand-name .name-main,
  .brand-name .name-sub { display: block; }
  .card-front .name-main { font-size: 30px; letter-spacing: 0.05em; }
  .card-front .name-sub { font-size: 15px; letter-spacing: 0.42em; margin-top: 4px; padding-left: 2px; }

  /* Back */
  .card-back { display: flex; align-items: center; }
  .back-brand {
    width: 330px;
    display: flex;
    justify-content: center;
  }
  .back-brand .brand-lockup { gap: 10px; }
  .back-brand .brand-mark { width: 14px; height: 14px; }
  .back-brand .name-main { font-size: 20px; letter-spacing: 0.04em; }
  .back-brand .name-sub { font-size: 11px; letter-spacing: 0.4em; margin-top: 3px; padding-left: 1px; }
  .divider {
    width: 1px;
    height: 230px;
    background: var(--rule);
  }
  .rep { padding-left: 40px; }
  .rep-name {
    color: var(--brand-blue);
    font-weight: 600;
    font-size: 26px;
    letter-spacing: 0.03em;
    text-transform: uppercase;
    white-space: nowrap;
  }
  .rep-title {
    color: var(--ink-soft);
    font-weight: 500;
    font-size: 14px;
    letter-spacing: 0.05em;
    text-transform: uppercase;
    margin-top: 2px;
  }
  .contact-list { list-style: none; margin-top: 26px; }
  .contact-list li {
    display: flex;
    align-items: flex-start;
    gap: 14px;
    color: var(--brand-blue);
    font-weight: 500;
    font-size: 14px;
    line-height: 1.35;
    margin-bottom: 10px;
    white-space: nowrap;
  }
  .contact-list svg { width: 18px; height: 18px; flex: none; fill: var(--brand-green); }
</style>
</head>
<body>

  <section class="card card-front" aria-label="Business card front">
    <div class="side-band side-band-left" role="img" aria-label="Soft blue decorative side panel"></div>
    <div class="side-band side-band-right" role="img" aria-label="Soft green decorative side panel"></div>
    <div class="brand-lockup">
      <span class="brand-mark"></span>
      <span class="brand-name">
        <span class="name-main">Harborline Crest</span>
        <span class="name-sub">Consulting</span>
      </span>
    </div>
  </section>

  <section class="card card-back" aria-label="Business card back">
    <div class="back-brand">
      <div class="brand-lockup">
        <span class="brand-mark"></span>
        <span class="brand-name">
          <span class="name-main">Harborline Crest</span>
          <span class="name-sub">Consulting</span>
        </span>
      </div>
    </div>
    <div class="divider"></div>
    <div class="rep">
      <h1 class="rep-name">Peter Vance</h1>
      <p class="rep-title">Managing Director</p>
      <ul class="contact-list">
        <li>
          <svg viewBox="0 0 24 24" aria-hidden="true"><path d="M6.6 10.8a15.1 15.1 0 0 0 6.6 6.6l2.2-2.2a1 1 0 0 1 1-.25 11.4 11.4 0 0 0 3.6.57 1 1 0 0 1 1 1V20a1 1 0 0 1-1 1A17 17 0 0 1 3 4a1 1 0 0 1 1-1h3.5a1 1 0 0 1 1 1c0 1.25.2 2.45.57 3.57a1 1 0 0 1-.25 1z"/></svg>
          <span>833-555-0172</span>
        </li>
        <li>
          <svg viewBox="0 0 24 24" aria-hidden="true"><path d="M2 5h20v14H2z M4 7v.4l8 5.2 8-5.2V7z" fill-rule="evenodd"/></svg>
          <span>pvance@harborlinecrest.com</span>
        </li>
        <li>
          <svg viewBox="0 0 24 24" aria-hidden="true"><path d="M12 2a10 10 0 1 0 0 20 10 10 0 0 0 0-20zm6.9 9h-3a15 15 0 0 0-1.3-5.6A8 8 0 0 1 18.9 11zM12 4.1c.9 1.3 1.7 3.8 1.9 6.9h-3.8c.2-3.1 1-5.6 1.9-6.9zM9.4 5.4A15 15 0 0 0 8.1 11h-3a8 8 0 0 1 4.3-5.6zM5.1 13h3a15 15 0 0 0 1.3 5.6A8 8 0 0 1 5.1 13zm6.9 6.9c-.9-1.3-1.7-3.8-1.9-6.9h3.8c-.2 3.1-1 5.6-1.9 6.9zm2.6-1.3a15 15 0 0 0 1.3-5.6h3a8 8 0 0 1-4.3 5.6z"/></svg>
          <span>www.harborlinecrest.com</span>
        </li>
        <li>
          <svg viewBox="0 0 24 24" aria-hidden="true"><path d="M12 2a7 7 0 0 0-7 7c0 5.2 7 13 7 13s7-7.8 7-13a7 7 0 0 0-7-7zm0 9.5A2.5 2.5 0 1 1 12 6.5a2.5 2.5 0 0 1 0 5z"/></svg>
          <span>410-2200 Quayside Ave Vancouver,<br>BC, V6B 4N8</span>
        </li>
      </ul>
    </div>
  </section>

</body>
</html>
```